UK based Drone services needs a pdf / flyer designed.

I am looking to get a flyer advertising what we do. I have added a word document with a little background and what services we offer, please could you add images for each service if possible? We are NPB approved and would like that to be mentioned on the bottom right corner please (logo attached). All our work is carried out with TQX drones, so would ideally like maybe a TQX Halvorn 620 rtk image in there. BrixtonUAV is the name of the company. Please get back to me if you have any questions.

```html
<!DOCTYPE html>
<html lang="en">
<head>
<meta charset="utf-8">
<title>BrixtonUAV Flyer</title>
<link href="https://fonts.googleapis.com/css2?family=Anton&family=Poppins:wght@400;600;700&family=Arimo:wght@400;700&display=swap" rel="stylesheet">
<style>
:root{
  --page-bg:#3a3a3a;
  --paper:#ffffff;
  --ink:#111111;
  --navy:#1d4a6b;
  --navy-dark:#153a56;
  --steel:#5c7d96;
  --grey-box:#e4e4e4;
  --rule:#cfcfcf;
}
*{margin:0;padding:0;box-sizing:border-box}
html,body{width:1200px;height:3111px;overflow:hidden;background:var(--page-bg)}
.flyer{
  position:absolute;left:50px;top:844px;width:820px;height:1060px;
  background:var(--paper);transform:scale(1.3415);transform-origin:0 0;overflow:hidden;
  font-family:'Arimo',Arial,sans-serif;color:var(--ink);
}
.shapes{position:absolute;left:0;top:0;width:820px;height:1060px}
.abs{position:absolute}
.brand{left:118px;top:48px;display:flex;align-items:center;gap:8px;
  font-family:'Poppins',sans-serif;font-weight:700;font-size:26px;color:#6b6b6b}
.brand-dot{width:14px;height:14px;border-radius:50%;background:#6b6b6b}
.headline{left:62px;top:134px;font-family:'Anton',sans-serif;font-size:51px;line-height:51px;letter-spacing:.5px;color:var(--ink)}
.subline{left:62px;top:293px;font-family:'Poppins',sans-serif;font-weight:700;font-size:18px;line-height:22px;color:var(--navy)}
.subline .dark{color:var(--ink)}
.band-text{left:65px;top:383px;width:720px;color:#fff;font-size:13.5px;line-height:17px}
.model-label{left:147px;top:469px;font-family:'Poppins',sans-serif;font-weight:600;font-size:15px;line-height:19px;color:#fff}
.point{font-size:11px;line-height:13px;color:#222;width:450px}
.summary{font-size:11px;line-height:13px;color:#222;background:var(--grey-box);border-radius:8px;padding:8px 10px 6px 30px}
.summary::before{content:"";position:absolute;left:14px;top:12px;width:7px;height:7px;border-radius:50%;background:#222}
.services-tab{left:86px;top:775px;width:236px;height:28px;background:var(--navy);color:#fff;
  font-family:'Poppins',sans-serif;font-size:19px;line-height:28px;padding-left:14px;
  clip-path:polygon(0 0,93% 0,100% 100%,0 100%)}
.services-tab b{font-weight:700}
.tile{width:167px}
.tile-cap{background:#111;color:#fff;font-family:'Poppins',sans-serif;font-weight:600;font-size:10.5px;height:20px;line-height:20px;text-align:center}
.badge-shape{left:640px;top:830px;width:88px;height:88px;background:var(--navy);border-radius:4px}
.badge-text{left:628px;top:924px;width:112px;text-align:center;font-family:'Poppins',sans-serif;font-weight:700;font-size:11px;line-height:12px;color:var(--steel)}
.badge-text span{color:var(--navy)}
.contact{font-family:'Poppins',sans-serif;color:#fff;display:flex;align-items:center;gap:8px;white-space:nowrap}
.phone{left:86px;top:1018px;font-size:19px;font-weight:600}
.mail{left:316px;top:1026px;font-size:14px}
.web{left:566px;top:1026px;font-size:14px}
</style>
</head>
<body>
<div class="flyer">
  <svg class="shapes" viewBox="0 0 820 1060">
    <defs>
      <linearGradient id="heroTone" x1="0" y1="0" x2="1" y2="1">
        <stop offset="0" stop-color="#6f8ea6"/>
        <stop offset=".5" stop-color="#2e4d66"/>
        <stop offset="1" stop-color="#1a2f40"/>
      </linearGradient>
      <radialGradient id="discTone" cx=".5" cy=".4" r=".6">
        <stop offset="0" stop-color="#3e6e96"/>
        <stop offset="1" stop-color="#15314d"/>
      </radialGradient>
      <linearGradient id="fieldTone" x1="0" y1="0" x2="0" y2="1">
        <stop offset="0" stop-color="#6e8f4f"/><stop offset="1" stop-color="#2f4a22"/>
      </linearGradient>
      <linearGradient id="cropTone" x1="0" y1="0" x2="0" y2="1">
        <stop offset="0" stop-color="#a8c98a"/><stop offset="1" stop-color="#3f8a2a"/>
      </linearGradient>
      <linearGradient id="workerTone" x1="0" y1="0" x2="1" y2="1">
        <stop offset="0" stop-color="#c9b79a"/><stop offset="1" stop-color="#6a6f73"/>
      </linearGradient>
      <linearGradient id="panelTone" x1="0" y1="0" x2="1" y2="1">
        <stop offset="0" stop-color="#9fb3c7"/><stop offset="1" stop-color="#34475c"/>
      </linearGradient>
      <linearGradient id="deskTone" x1="0" y1="0" x2="1" y2="1">
        <stop offset="0" stop-color="#efefef"/><stop offset="1" stop-color="#bdbdbd"/>
      </linearGradient>
    </defs>

    <polygon points="383,0 668,0 820,230 820,290 560,350" fill="url(#heroTone)" role="img" aria-label="Quadcopter drone with glowing lights hovering over a misty forest"/>
    <polygon points="668,0 820,0 820,230" fill="#0d0d0d"/>
    <polygon points="415,358 490,220 540,358" fill="#2a2a2a" role="img" aria-label="Dark grassy texture panel"/>

    <rect x="0" y="372" width="820" height="60" fill="#000"/>

    <circle cx="190" cy="572" r="110" fill="url(#discTone)" role="img" aria-label="TQX Halvorn 620 rtk drone with its remote controller"/>
    <path d="M190 450 A122 122 0 0 1 190 694" fill="none" stroke="#111" stroke-width="7"/>

    <g fill="#fff" stroke="#111" stroke-width="3">
      <circle cx="280" cy="482" r="22"/>
      <circle cx="312" cy="540" r="22"/>
      <circle cx="306" cy="598" r="22"/>
      <circle cx="276" cy="653" r="22"/>
    </g>
    <g fill="none" stroke="#111" stroke-width="1.6">
      <rect x="272" y="478" width="16" height="8" rx="2"/><path d="M266 476h8M286 476h8M280 486v5"/>
      <rect x="302" y="533" width="20" height="14" rx="1"/><path d="M310 537l6 3-6 3z" fill="#111"/>
      <circle cx="302" cy="594" r="5"/><rect x="306" y="598" width="10" height="9"/><path d="M296 607h8"/>
      <path d="M268 646h10l4 4v11h-14z"/><path d="M271 654h8M271 658h8"/>
    </g>

    <g stroke="var(--rule)" stroke-width="1">
      <line x1="343" y1="510" x2="755" y2="510"/>
      <line x1="343" y1="570" x2="755" y2="570"/>
      <line x1="313" y1="630" x2="755" y2="630"/>
    </g>

    <rect x="86" y="810" width="167" height="66" fill="url(#workerTone)" role="img" aria-label="Engineer in hard hat and hi-vis vest on site"/>
    <rect x="261" y="810" width="167" height="66" fill="url(#fieldTone)" role="img" aria-label="Aerial view of a winding road through woodland with a location pin"/>
    <rect x="438" y="810" width="167" height="66" fill="url(#fieldTone)" role="img" aria-label="Drone flying low over a green meadow"/>
    <rect x="86" y="906" width="167" height="66" fill="url(#panelTone)" role="img" aria-label="Two engineers inspecting solar panels"/>
    <rect x="261" y="906" width="167" height="68" fill="url(#deskTone)" role="img" aria-label="Architectural drawings with pencil and magnifier on a desk"/>
    <rect x="438" y="906" width="167" height="66" fill="url(#cropTone)" role="img" aria-label="Rows of young green crops in a field"/>

    <polygon points="0,1010 280,1010 300,1060 0,1060" fill="var(--navy)"/>
    <polygon points="280,1018 820,1018 820,1060 300,1060" fill="#000"/>
    <polygon points="270,1010 282,1010 302,1060 290,1060" fill="#fff"/>
  </svg>

  <div class="abs brand"><span class="brand-dot"></span>BrixtonUAV</div>

  <h1 class="abs headline">ELEVATE YOUR<br>VISION WITH<br>BRIXTONUAV</h1>
  <p class="abs subline">Are revolutionizing the<br>wayindustries are able to work.<br><span class="dark">Unmanned Arial Vehicles (UAV's)</span></p>

  <p class="abs band-text">With current advances in technology, drones are opening doors that weren't available before. With the ability to reach difficult and dangerous areas, they remove the human element and change the scope of what's safely possible.</p>

  <p class="abs model-label">TQX Halvorn<br>620 rtk</p>

  <p class="abs point" style="left:313px;top:460px">BrixtonUAV is fully equipped with the latest and most suitable drones for your business or personal needs. From a small roof survey to a full wind turbine site inspection. No project is too small or too large, take advantage of using UAV's now!</p>
  <p class="abs point" style="left:343px;top:520px">Capturing live Ultra High-Definition footage of unreachable areas and making working at heights a thing of the past. Drones are safer, faster, more cost-effective and a highly accurate alternative.</p>
  <p class="abs point" style="left:343px;top:585px">Not only do you have the chance to inspect dangerous areas live, but you also get photographs and/or 4K Ultra HD video footage to review at a later date.</p>
  <p class="abs point" style="left:313px;top:648px">No need to send someone back out to the area to double-check damage, you have it all on record.</p>

  <p class="abs summary" style="left:65px;top:700px;width:350px">Here at BrixtonUAV, we pride ourselves on being affordable and offering a great product to our clients. We have a comprehensive list of services that we offer to any business or individual across the UK.</p>
  <p class="abs summary" style="left:420px;top:700px;width:336px">Our UAV pilots are GVC licensed and have gained Operational Authorization from the National Pilot Board allowing us to carry out commercial work in the UK.</p>

  <div class="abs services-tab">SERVICES <b>WE OFFER</b></div>

  <div class="abs tile" style="left:86px;top:876px"><div class="tile-cap">Commercial Inspections</div></div>
  <div class="abs tile" style="left:261px;top:876px"><div class="tile-cap">Mapping / Surveys</div></div>
  <div class="abs tile" style="left:438px;top:876px"><div class="tile-cap">Arial Photography</div></div>
  <div class="abs tile" style="left:86px;top:972px"><div class="tile-cap">Solar Panel Inspections</div></div>
  <div class="abs tile" style="left:261px;top:974px"><div class="tile-cap">Real Estate / Planning</div></div>
  <div class="abs tile" style="left:438px;top:972px"><div class="tile-cap">Agriculture</div></div>

  <div class="abs badge-shape" role="img" aria-label="Approval badge"></div>
  <p class="abs badge-text">WE ARE NPB<br><span>APPROVED</span></p>

  <div class="abs contact phone">
    <svg width="18" height="18" viewBox="0 0 24 24" aria-hidden="true"><path d="M6.6 10.8a15 15 0 0 0 6.6 6.6l2.2-2.2a1 1 0 0 1 1-.25 11.4 11.4 0 0 0 3.6.57 1 1 0 0 1 1 1V20a1 1 0 0 1-1 1A17 17 0 0 1 3 4a1 1 0 0 1 1-1h3.5a1 1 0 0 1 1 1c0 1.25.2 2.45.57 3.57a1 1 0 0 1-.25 1z" fill="#fff"/></svg>
    07700 900418
  </div>
  <div class="abs contact mail">
    <svg width="16" height="14" viewBox="0 0 24 20" aria-hidden="true"><rect x="1" y="2" width="22" height="16" rx="2" fill="none" stroke="#fff" stroke-width="2"/><path d="M1 3l11 8 11-8" fill="none" stroke="#fff" stroke-width="2"/></svg>
    brixtonuav@inboxmail.com
  </div>
  <div class="abs contact web">
    <svg width="16" height="16" viewBox="0 0 24 24" aria-hidden="true"><circle cx="12" cy="12" r="10" fill="none" stroke="#fff" stroke-width="2"/><path d="M2 12h20M12 2c3 3 3 17 0 20M12 2c-3 3-3 17 0 20" fill="none" stroke="#fff" stroke-width="1.6"/></svg>
    www.brixtonuav.com
  </div>
</div>
</body>
</html>
```